Manufacturing company needs new business card.

I need a unique Business Card that will truly stand out. Nothing too busy. Simple is good, right? Not looking for a standard design either. No cookie cutter layout. I am just looking for something interesting and a bit different. Does't have to completely off the wall crazy, just not your run of the mill business card. Clean and modern with a touch of industrial.

Target Market(s)

Air conditioning industry, Architects, builders.

Industry/Entity Type

Business

Contact Information for Business Card

Details to be included on card are:

Peter Vance
Managing Director

T: 1300 847 519
M: 0428 593 174
W: www.brenvaleworks.com.au
E: peter.vance@brenvaleworks.com.au
A: 58 Harwick Lane, Sydney NSW 2000

Font styles to use
Sans Serif

Colors
0355a3
848484
fbfbfb

Requirements
Must have
• Card design must be landscape.

```html
<!DOCTYPE html>
<html lang="en">
<head>
<meta charset="utf-8">
<title>Brenvale Works – Business Card</title>
<link href="https://fonts.googleapis.com/css2?family=Open+Sans:wght@400;600;700&display=swap" rel="stylesheet">
<style>
  :root {
    --brand-blue: #0355a3;
    --brand-blue-bright: #2756b8;
    --brand-grey: #848484;
    --paper: #fbfbfb;
    --card-black: #030303;
    --stage: #2a2a2a;
    --text-light: #c9c9c9;
  }
  * { margin: 0; padding: 0; box-sizing: border-box; }
  html, body {
    width: 1200px; height: 900px; overflow: hidden;
    background: var(--stage);
    font-family: "Open Sans", Arial, sans-serif;
  }
  .stage {
    position: relative; width: 1200px; height: 900px;
    display: flex; flex-direction: column; align-items: center; justify-content: center;
    gap: 56px;
  }
  .card {
    position: relative; width: 560px; height: 320px;
    border-radius: 24px; overflow: hidden;
    box-shadow: 0 10px 30px rgba(0,0,0,.45);
  }

  /* Front */
  .card-front { background: var(--paper); }
  .front-brand {
    position: absolute; left: 84px; top: 92px;
    display: flex; align-items: center; gap: 18px;
  }
  .brand-square { width: 26px; height: 26px; background: var(--brand-grey); }
  .brand-name {
    font-weight: 600; font-size: 40px; letter-spacing: -0.5px;
    color: var(--brand-blue-bright); line-height: 1;
  }
  .front-rule {
    position: absolute; left: 128px; top: 160px;
    width: 360px; height: 2px; background: var(--brand-grey);
  }
  .front-web {
    position: absolute; left: 0; right: 0; top: 232px;
    display: flex; align-items: center; gap: 12px;
  }
  .front-web .line { flex: 1; height: 2px; background: var(--brand-grey); }
  .front-web .url { font-size: 13px; color: var(--brand-blue-bright); white-space: nowrap; }
  .front-base {
    position: absolute; left: 0; right: 0; top: 272px;
    height: 2px; background: var(--brand-grey);
  }

  /* Back */
  .card-back { background: var(--card-black); color: var(--text-light); }
  .back-brand {
    position: absolute; left: 36px; top: 36px;
    display: flex; align-items: center; gap: 14px;
  }
  .back-brand .brand-name { font-size: 34px; }
  .back-brand .brand-square { width: 22px; height: 22px; }
  .back-rule {
    position: absolute; left: 36px; top: 92px;
    width: 300px; height: 2px; background: var(--brand-grey);
  }
  .person { position: absolute; left: 48px; top: 110px; }
  .person-name { font-weight: 700; font-size: 17px; color: var(--brand-blue-bright); }
  .person-role { font-size: 14px; color: var(--text-light); margin-top: 2px; }
  .contacts {
    position: absolute; left: 48px; top: 170px; list-style: none;
  }
  .contacts li {
    display: flex; align-items: center; gap: 8px;
    font-size: 14px; line-height: 21px; color: var(--text-light);
  }
  .contacts svg { width: 15px; height: 15px; flex: none; }
  .address {
    position: absolute; left: 48px; top: 268px;
    font-size: 14px; color: var(--brand-blue-bright);
  }
</style>
</head>
<body>
<main class="stage">

  <section class="card card-front" aria-label="Business card front">
    <div class="front-brand">
      <span class="brand-square"></span>
      <span class="brand-name">Brenvale Works</span>
    </div>
    <div class="front-rule"></div>
    <div class="front-web">
      <span class="line"></span>
      <span class="url">www.brenvaleworks.com.au</span>
      <span class="line" style="flex:0.25"></span>
    </div>
    <div class="front-base"></div>
  </section>

  <section class="card card-back" aria-label="Business card back">
    <div class="back-brand">
      <span class="brand-name">Brenvale Works</span>
      <span class="brand-square"></span>
    </div>
    <div class="back-rule"></div>

    <div class="person">
      <div class="person-name">Peter Vance</div>
      <div class="person-role">Managing Director</div>
    </div>

    <ul class="contacts">
      <li>
        <svg viewBox="0 0 16 16" aria-hidden="true"><rect width="16" height="16" rx="2" fill="#2756b8"/><path d="M5 3.5l2 2-1 1.2c.6 1.3 1.6 2.3 2.9 2.9l1.2-1 2 2-1.1 1.6C7.6 12 4 8.4 3.8 4.6z" fill="#fbfbfb"/></svg>
        1300 847 519
      </li>
      <li>
        <svg viewBox="0 0 16 16" aria-hidden="true"><rect width="16" height="16" rx="2" fill="#2756b8"/><rect x="5" y="3" width="6" height="10" rx="1" fill="none" stroke="#fbfbfb" stroke-width="1.3"/></svg>
        0428 593 174
      </li>
      <li>
        <svg viewBox="0 0 16 16" aria-hidden="true"><rect width="16" height="16" rx="2" fill="#2756b8"/><rect x="3" y="4.5" width="10" height="7" fill="none" stroke="#fbfbfb" stroke-width="1.2"/><path d="M3 4.5l5 4 5-4" fill="none" stroke="#fbfbfb" stroke-width="1.2"/></svg>
        peter.vance@brenvaleworks.com.au
      </li>
      <li>
        <svg viewBox="0 0 16 16" aria-hidden="true"><rect width="16" height="16" rx="2" fill="#2756b8"/><circle cx="8" cy="8" r="4.8" fill="none" stroke="#fbfbfb" stroke-width="1.1"/><path d="M3.2 8h9.6M8 3.2c-2.4 2.8-2.4 6.8 0 9.6M8 3.2c2.4 2.8 2.4 6.8 0 9.6" fill="none" stroke="#fbfbfb" stroke-width="1"/></svg>
        www.brenvaleworks.com.au
      </li>
    </ul>

    <div class="address">58 Harwick Lane, Sydney NSW 2000</div>
  </section>

</main>
</body>
</html>
```